Health care technology software systems

We have a solid logo. We have company colors that will need to be used as well. We just need a great business card design. We sell to health plans but want to be modern
Updates

Need extra days to review

Target Market(s)

Health technology sector selling into Health Plans

Industry/Entity Type

Health Care Technology

Contact Information for Business Card

Name, title, address, phone number, email

Requirements
Must have
• Use of Kembrata corporate colors - Uploaded w/ our logos

```html
<!DOCTYPE html>
<html lang="en">
<head>
<meta charset="utf-8">
<title>Kembrata Business Card</title>
<link href="https://fonts.googleapis.com/css2?family=Montserrat:wght@300;400;500;700&display=swap" rel="stylesheet">
<style>
  :root {
    --brand-navy: #3a539e;
    --brand-sky: #2ea7e0;
    --brand-green: #8cc63f;
    --ink: #1f1f1f;
    --wordmark-grey: #3c3c3c;
    --paper: #ffffff;
    --stage: #4a4a4a;
  }
  html, body {
    margin: 0;
    padding: 0;
    width: 1200px;
    height: 1021px;
    overflow: hidden;
    background: var(--stage);
    font-family: "Montserrat", sans-serif;
  }
  .stage {
    position: relative;
    width: 1200px;
    height: 1021px;
  }
  .card {
    position: absolute;
    left: 233px;
    width: 740px;
    height: 427px;
    border-radius: 24px;
    overflow: hidden;
  }
  .card-front {
    top: 65px;
    background: var(--paper);
  }
  .card-back {
    top: 511px;
    background: var(--brand-navy);
  }

  /* front */
  .brand-lockup {
    position: absolute;
    left: 58px;
    top: 62px;
    display: flex;
    align-items: center;
    gap: 18px;
  }
  .brand-dot {
    width: 46px;
    height: 46px;
    border-radius: 50%;
    background: var(--brand-sky);
  }
  .brand-name {
    font-weight: 300;
    font-size: 48px;
    line-height: 1;
    color: var(--wordmark-grey);
    letter-spacing: 0.5px;
  }
  .person-name {
    position: absolute;
    left: 57px;
    top: 150px;
    margin: 0;
    font-weight: 700;
    font-size: 24px;
    color: var(--brand-sky);
    letter-spacing: 0.2px;
  }
  .person-title {
    position: absolute;
    left: 57px;
    top: 181px;
    margin: 0;
    font-weight: 400;
    font-size: 24px;
    color: var(--ink);
  }
  .address {
    position: absolute;
    left: 56px;
    top: 236px;
    margin: 0;
    font-style: normal;
    font-weight: 400;
    font-size: 18px;
    line-height: 27px;
    color: var(--ink);
  }
  .contact-list {
    position: absolute;
    left: 56px;
    top: 308px;
    margin: 0;
    padding: 0;
    list-style: none;
  }
  .contact-list li {
    display: flex;
    align-items: center;
    height: 30px;
    font-size: 18px;
    color: var(--ink);
  }
  .contact-list svg {
    width: 20px;
    height: 20px;
    margin-right: 11px;
    flex: none;
  }
  .brand-emblem {
    position: absolute;
    left: 368px;
    top: 33px;
    width: 348px;
    height: 348px;
    border-radius: 50%;
    background: radial-gradient(circle, #e8f4fb 0%, #cfe7f5 100%);
  }

  /* back */
  .back-lockup {
    position: absolute;
    left: 0;
    right: 0;
    top: 170px;
    display: flex;
    justify-content: center;
    align-items: center;
    gap: 30px;
  }
  .back-lockup .brand-dot {
    width: 80px;
    height: 80px;
    background: var(--paper);
  }
  .back-lockup .brand-name {
    font-size: 82px;
    color: var(--paper);
  }
</style>
</head>
<body>
<main class="stage">
  <section class="card card-front" aria-label="Business card front">
    <div class="brand-lockup">
      <span class="brand-dot"></span>
      <span class="brand-name">kembrata</span>
    </div>
    <h1 class="person-name">DORIN HALVESEN</h1>
    <p class="person-title">Co-Founder</p>
    <address class="address">4180 N. Harbor Lane<br>Suite 2207 Calverton.41</address>
    <ul class="contact-list">
      <li>
        <svg viewBox="0 0 20 20" aria-hidden="true"><path fill="var(--brand-sky)" d="M4.5 2.5l3 3.2-1.6 2a10 10 0 0 0 6.4 6.4l2-1.6 3.2 3-1.8 2.4C9.5 18 2 10.5 2.1 4.3z"/><path fill="none" stroke="var(--brand-sky)" stroke-width="1.4" d="M11.5 4.5a4 4 0 0 1 4 4M11.5 1.5a7 7 0 0 1 7 7"/></svg>
        555-214-7390
      </li>
      <li>
        <svg viewBox="0 0 20 20" aria-hidden="true"><rect x="1.5" y="4" width="17" height="12" fill="var(--brand-sky)"/><path d="M1.5 4.5l8.5 6.5 8.5-6.5M1.5 15.5l6-5M18.5 15.5l-6-5" fill="none" stroke="#fff" stroke-width="1.2"/></svg>
        info@kembrata.com
      </li>
      <li>
        <svg viewBox="0 0 20 20" aria-hidden="true"><circle cx="10" cy="10" r="8.5" fill="var(--brand-sky)"/><path d="M6 5c2 1 1 3 3 3s1 3-1 4-1 3-2 3M13 4c-1 2 1 3 2 3s1 2 0 3-2 1-1 3" fill="none" stroke="#fff" stroke-width="1.3"/></svg>
        www.kembrata.com
      </li>
    </ul>
    <div class="brand-emblem" role="img" aria-label="Large brand emblem area"></div>
  </section>

  <section class="card card-back" aria-label="Business card back">
    <div class="back-lockup">
      <span class="brand-dot"></span>
      <span class="brand-name">kembrata</span>
    </div>
  </section>
</main>
</body>
</html>
```